Business Card - connecting 2 souls and beggining the journey of self discovery

Logo on the front
with tag line

On the back list of services and contact details

Seminars
workshops
Coaching
podcasts

Daniel Porthwick
Health & Wellbeing Life Coach
0491 372 815
daniel@wovenpathwellness.example
wovenpathwellness.example

Industry/Entity Type

Life Coaching

Contact Information for Business Card

I like the use of colour from the logo to be used. I'm not a fan of white.

Requirements
Must have
• My tagline: The journey home starts with you
Nice to have
• Use of colour that is in the mind body soul logo

```html
<!DOCTYPE html>
<html lang="en">
<head>
<meta charset="utf-8">
<title>Woven Path Wellness – Business Card</title>
<link rel="stylesheet" href="https://fonts.googleapis.com/css2?family=Montserrat:wght@500;600;700&family=Open+Sans:wght@300;400&display=swap">
<style>
  :root {
    --bg: #2a2c30;
    --card: #ffffff;
    --purple: #7b4fa3;
    --pink: #e9536b;
    --teal: #2fa99c;
  }
  * { box-sizing: border-box; margin: 0; padding: 0; }
  html, body { width: 1200px; height: 900px; overflow: hidden; }
  body {
    background: var(--bg);
    position: relative;
    font-family: "Open Sans", sans-serif;
  }
  .card {
    position: absolute;
    background: var(--card);
    border-radius: 28px;
    overflow: hidden;
    box-shadow: 0 18px 40px rgba(0,0,0,.45);
  }

  /* ---------- contact side ---------- */
  .card-contact { left: 90px; top: 139px; width: 380px; height: 622px; }
  .card-contact .bands { position: absolute; inset: 0; }
  .contact-body {
    position: relative;
    display: flex; flex-direction: column; align-items: center;
    text-align: center;
    padding-top: 36px;
  }
  .brand {
    display: flex; flex-direction: column; align-items: center; gap: 12px;
  }
  .brand-dot {
    width: 74px; height: 74px; border-radius: 50%;
    background: var(--purple);
  }
  .brand-name {
    font-family: "Montserrat", sans-serif;
    font-weight: 700; font-size: 22px;
    line-height: 1.2;
    color: var(--purple);
    letter-spacing: -0.3px;
  }
  .tagline {
    margin-top: 6px;
    font-family: "Montserrat", sans-serif;
    font-weight: 500; font-size: 13px;
    color: var(--purple);
  }
  .person-name {
    margin-top: 24px;
    font-family: "Montserrat", sans-serif;
    font-weight: 700; font-size: 32px;
    letter-spacing: -0.5px;
    line-height: 1;
  }
  .person-name .first { color: var(--pink); }
  .person-name .last { color: var(--purple); font-weight: 600; }
  .role {
    margin-top: 8px;
    font-family: "Montserrat", sans-serif;
    font-weight: 500; font-size: 13px;
    color: var(--purple);
  }
  .icons { display: flex; gap: 12px; margin-top: 16px; }
  .icon {
    width: 34px; height: 34px; border-radius: 50%;
    background: var(--pink);
    display: flex; align-items: center; justify-content: center;
  }
  .icon svg { width: 18px; height: 18px; }
  .details {
    margin-top: 12px;
    list-style: none;
    font-family: "Montserrat", sans-serif;
    font-weight: 500; font-size: 13.5px;
    line-height: 1.6;
    color: var(--purple);
  }

  /* ---------- services side ---------- */
  .card-services { left: 520px; top: 260px; width: 622px; height: 380px; }
  .services-brand {
    position: absolute; left: 60px; top: 0; bottom: 0; width: 250px;
    display: flex; flex-direction: column; align-items: center; justify-content: center;
  }
  .services-brand .brand-dot { width: 80px; height: 80px; }
  .services-brand .brand-name { font-size: 21px; margin-top: 4px; }
  .divider { position: absolute; left: 330px; top: 60px; width: 40px; height: 260px; }
  .services {
    position: absolute; left: 400px; top: 50%; transform: translateY(-50%);
    list-style: none;
    font-family: "Open Sans", sans-serif;
    font-weight: 400; font-size: 30px;
    line-height: 1.05;
    color: var(--purple);
  }
</style>
</head>
<body>

  <section class="card card-contact">
    <svg class="bands" viewBox="0 0 380 622" preserveAspectRatio="none" aria-hidden="true">
      <path d="M0 502 Q210 484 380 404 L380 622 L0 622 Z" fill="var(--pink)"/>
      <path d="M0 516 Q220 498 380 416 L380 622 L0 622 Z" fill="var(--teal)"/>
      <path d="M0 532 Q230 514 380 430 L380 622 L0 622 Z" fill="var(--purple)"/>
    </svg>
    <div class="contact-body">
      <div class="brand">
        <span class="brand-dot"></span>
        <span class="brand-name">Woven Path Wellness</span>
      </div>
      <p class="tagline">The journey home starts with you</p>
      <h1 class="person-name"><span class="first">Daniel</span> <span class="last">Porthwick</span></h1>
      <p class="role">Health &amp; Wellbeing Life Coach</p>
      <div class="icons">
        <span class="icon">
          <svg viewBox="0 0 24 24"><path fill="#fff" d="M6.6 10.8a15 15 0 0 0 6.6 6.6l2.2-2.2c.3-.3.7-.4 1-.2 1.1.4 2.3.6 3.6.6.6 0 1 .4 1 1V20c0 .6-.4 1-1 1A17 17 0 0 1 3 4c0-.6.4-1 1-1h3.5c.6 0 1 .4 1 1 0 1.3.2 2.5.6 3.6.1.3 0 .7-.2 1z"/></svg>
        </span>
        <span class="icon">
          <svg viewBox="0 0 24 24" fill="none" stroke="#fff" stroke-width="2"><circle cx="12" cy="12" r="9"/><path d="M3 12h18M12 3c3 3 3 15 0 18M12 3c-3 3-3 15 0 18"/></svg>
        </span>
        <span class="icon">
          <svg viewBox="0 0 24 24" fill="none" stroke="#fff" stroke-width="2"><rect x="3" y="5" width="18" height="14" rx="1"/><path d="M3 6l9 7 9-7"/></svg>
        </span>
      </div>
      <ul class="details">
        <li>0491 372 815</li>
        <li>wovenpathwellness.example</li>
        <li>daniel@wovenpathwellness.example</li>
      </ul>
    </div>
  </section>

  <section class="card card-services">
    <div class="services-brand">
      <span class="brand-dot"></span>
      <span class="brand-name">Woven Path Wellness</span>
    </div>
    <svg class="divider" viewBox="0 0 40 260" aria-hidden="true">
      <defs>
        <linearGradient id="divider-fade" x1="0" y1="0" x2="0" y2="1">
          <stop offset="0" stop-color="#e9536b" stop-opacity="0"/>
          <stop offset="0.5" stop-color="#e9536b" stop-opacity="1"/>
          <stop offset="1" stop-color="#e9536b" stop-opacity="0"/>
        </linearGradient>
      </defs>
      <line x1="38" y1="0" x2="2" y2="260" stroke="url(#divider-fade)" stroke-width="2"/>
    </svg>
    <ul class="services">
      <li>Seminars</li>
      <li>workshops</li>
      <li>Coaching</li>
      <li>podcasts</li>
    </ul>
  </section>

</body>
</html>
```